Re-design of Business Card

We require a design for our business card.

Korrim is a supplier of industrial packaging specializing in plastic products. We are undergoing a rebranding to appear more corporate. We have changed our company name to korrim and have a new logo.

I have uploaded our old card design with the previous company name.
Don't copy the current design. We are looking for a new design.

Industry/Entity Type

Manufacturing

Contact Information for Business Card

please don't copy the current design. we are looking for a new design.

Font styles to use
Sans Serif

Colors

Designer to choose colors to be used in the design.

Requirements
Must have
• clean and easy to read.

```html
<!DOCTYPE html>
<html lang="en">
<head>
<meta charset="utf-8">
<title>Korrim Business Card</title>
<link rel="stylesheet" href="https://fonts.googleapis.com/css2?family=Lato:wght@400;700;900&display=swap">
<style>
  :root {
    --orange: #ec9a22;
    --orange-deep: #d97d14;
    --grey: #6b6b6d;
    --grey-dark: #58585a;
    --white: #f4f4f4;
    --ink-light: #ffffff;
    --stage: #e9e6e1;
  }
  * { box-sizing: border-box; margin: 0; padding: 0; }
  html, body { width: 1200px; height: 780px; overflow: hidden; }
  body {
    background: var(--stage);
    font-family: "Lato", Arial, sans-serif;
    position: relative;
  }
  .card { position: absolute; overflow: hidden; box-shadow: 0 10px 30px rgba(0,0,0,.18); }

  /* Front */
  .card-front { left: 60px; top: 200px; width: 640px; height: 366px; background: var(--white); }
  .front-brand {
    position: absolute; left: 0; top: 0; width: 390px; height: 222px;
    display: flex; align-items: center; justify-content: center; gap: 14px;
  }
  .brand-square { width: 26px; height: 26px; background: var(--orange); }
  .brand-name {
    font-weight: 900; font-size: 66px; letter-spacing: 2px; color: var(--orange);
  }
  .front-contact {
    position: absolute; right: 0; top: 0; width: 250px; height: 366px;
    background: linear-gradient(160deg, var(--orange) 0%, var(--orange-deep) 100%);
    color: var(--ink-light); padding: 40px 26px; font-size: 15px; line-height: 1.55;
  }
  .front-person {
    position: absolute; left: 0; bottom: 0; width: 390px; height: 144px;
    background: var(--grey); color: var(--ink-light); padding: 22px 34px;
  }
  .person-name { font-weight: 700; font-size: 30px; line-height: 1.1; }
  .person-role { font-size: 15px; margin-bottom: 14px; }
  .row { display: flex; align-items: center; gap: 8px; font-size: 15px; line-height: 1.6; }
  .dot {
    width: 18px; height: 18px; border-radius: 50%; flex: none;
    display: flex; align-items: center; justify-content: center;
  }
  .dot-orange { background: var(--orange); }
  .dot-white { background: var(--ink-light); }
  .address { margin-bottom: 12px; }

  /* Back */
  .card-back { left: 770px; top: 100px; width: 370px; height: 640px; background: var(--orange); }
  .back-header {
    height: 130px; background: var(--grey-dark);
    display: flex; align-items: center; justify-content: center; gap: 12px;
  }
  .back-header .brand-square { background: var(--ink-light); width: 22px; height: 22px; }
  .back-header .brand-name { color: var(--ink-light); font-size: 56px; }
  .back-body {
    position: relative; height: 510px;
    background: linear-gradient(170deg, var(--orange) 0%, var(--orange-deep) 100%);
    color: var(--ink-light); padding: 26px 30px;
  }
  .map-backdrop {
    position: absolute; right: 20px; top: 40px; width: 230px; height: 270px;
    border-radius: 40% 50% 45% 55%;
    background: radial-gradient(circle, rgba(255,255,255,.16), rgba(255,255,255,0) 70%);
  }
  .service { position: relative; margin-bottom: 12px; }
  .service-title { font-weight: 700; font-size: 15px; letter-spacing: .5px; text-transform: uppercase; }
  .service-list { list-style: none; font-size: 14px; line-height: 1.35; }
  .service-list li::before { content: "• "; }
  .badges {
    position: absolute; left: 0; right: 0; bottom: 28px;
    display: flex; justify-content: space-around; padding: 0 20px;
  }
  .badge {
    width: 86px; height: 86px; border-radius: 50%;
    border: 3px solid rgba(255,255,255,.85);
  }
</style>
</head>
<body>
  <section class="card card-front" aria-label="Business card front">
    <div class="front-brand">
      <span class="brand-square"></span>
      <span class="brand-name">KORRIM</span>
    </div>
    <div class="front-contact">
      <p class="address">48 Marlow Rd<br>Brookfield Vale, Qld<br>4120 Australia</p>
      <p class="row"><span class="dot dot-white"><svg width="10" height="10" viewBox="0 0 10 10"><path d="M2 1h2l1 2-1 1a5 5 0 0 0 2 2l1-1 2 1v2a1 1 0 0 1-1 1A8 8 0 0 1 1 2a1 1 0 0 1 1-1z" fill="#ec9a22"/></svg></span>1300 415 862</p>
      <p class="row"><span class="dot dot-white"><svg width="10" height="10" viewBox="0 0 10 10"><path d="M2 1h2l1 2-1 1a5 5 0 0 0 2 2l1-1 2 1v2a1 1 0 0 1-1 1A8 8 0 0 1 1 2a1 1 0 0 1 1-1z" fill="#ec9a22"/></svg></span>+61 7 3380 2741</p>
      <p class="row"><span class="dot dot-white"><svg width="10" height="10" viewBox="0 0 10 10"><circle cx="5" cy="5" r="4" fill="none" stroke="#ec9a22" stroke-width="1.2"/><path d="M1 5h8M5 1v8" stroke="#ec9a22" stroke-width="1"/></svg></span>www.korrim.com.au</p>
    </div>
    <div class="front-person">
      <p class="person-name">Dylan Harrow</p>
      <p class="person-role">Machinery Sales Manager</p>
      <p class="row"><span class="dot dot-orange"><svg width="8" height="10" viewBox="0 0 8 10"><rect x="1" y="0.5" width="6" height="9" rx="1" fill="none" stroke="#fff" stroke-width="1.2"/></svg></span>xxxx xxx xxx</p>
      <p class="row"><span class="dot dot-orange"><svg width="10" height="8" viewBox="0 0 10 8"><rect x="0.5" y="0.5" width="9" height="7" fill="none" stroke="#fff" stroke-width="1.1"/><path d="M.5 .5l4.5 4 4.5-4" fill="none" stroke="#fff" stroke-width="1.1"/></svg></span>Dylan@korrim.com.au</p>
    </div>
  </section>

  <section class="card card-back" aria-label="Business card back">
    <div class="back-header">
      <span class="brand-square"></span>
      <span class="brand-name">KORRIM</span>
    </div>
    <div class="back-body">
      <div class="map-backdrop" role="img" aria-label="Faint map of Australia with flag motif"></div>
      <div class="service">
        <p class="service-title">Pallet Containment</p>
        <ul class="service-list"><li>Stretch</li><li>Heat Shrink</li><li>Pallet Hood</li></ul>
      </div>
      <div class="service">
        <p class="service-title">Flexible Packaging</p>
        <ul class="service-list"><li>Bags &amp; Liners</li><li>Tube</li><li>Film &amp; Sheet</li><li>Printed Films (12 col)</li><li>Shrink Films</li></ul>
      </div>
      <div class="service">
        <p class="service-title">Pallet Wrapping Machinery</p>
        <ul class="service-list"><li>Semi &amp; Fully Auto Lines</li><li>Finance Options include Lease, Rent, pay per wrap</li></ul>
      </div>
      <div class="service">
        <p class="service-title">General Packaging</p>
      </div>
      <div class="badges">
        <span class="badge" role="img" aria-label="Certification badge"></span>
        <span class="badge" role="img" aria-label="Certification badge"></span>
        <span class="badge" role="img" aria-label="Distribution badge"></span>
      </div>
    </div>
  </section>
</body>
</html>
```